We want a hot New Design for our IT company Web Site

We have a basic website with some general information and lots of mostly words and generic pictures we want to make it look and feel a lot more modern and slick. The site needs to work on mobile devices as well as desktops.

Target Market(s)

Business customers

Industry/Entity Type

It Company

Coding

Coded - Design and coding required

Number of Pages Required

5+ page

Requirements
Must have
• Sleek new Design making it look and feel more modern and less boring
Nice to have
• If it can have a better flow to it rather then have the std Drop down menus it has now.

```html
<!DOCTYPE html>
<html lang="en">
<head>
<meta charset="utf-8">
<title>Norvale Solutions Group</title>
<link href="https://fonts.googleapis.com/css2?family=Open+Sans:wght@400;600;700&family=Oswald:wght@400;500&display=swap" rel="stylesheet">
<style>
:root{
  --blue:#1a5cb0;
  --blue-dark:#0d2f66;
  --navy:#0a2350;
  --ink:#2b2f36;
  --muted:#8a8f98;
  --line:#e3e6ea;
  --bg:#ffffff;
  --soft:#f4f6f9;
}
*{box-sizing:border-box;margin:0;padding:0}
html,body{width:1200px;height:2220px;overflow:hidden;background:var(--bg);font-family:"Open Sans",Arial,sans-serif;color:var(--ink)}
.page{position:relative;width:1200px;height:2220px}
.wrap{position:absolute;left:80px;width:1040px}

/* header */
.site-header{position:absolute;top:0;left:0;width:1200px;height:130px;background:#fff;box-shadow:0 2px 6px rgba(0,0,0,.08);z-index:2}
.site-header .corner{position:absolute;top:0;right:0}
.brand{position:absolute;left:80px;top:28px;display:flex;align-items:center;gap:12px}
.brand .mark{width:58px;height:58px;background:var(--blue)}
.brand .name{font-weight:700;font-size:34px;color:var(--blue);letter-spacing:1px}
.main-nav{position:absolute;right:120px;top:52px;display:flex;gap:34px;font-size:15px;font-weight:600;text-transform:uppercase;color:var(--ink)}
.main-nav .active{color:var(--blue)}
.main-nav .sep{width:1px;height:20px;background:var(--line)}

/* hero */
.hero{position:absolute;top:130px;left:0;width:1200px;height:630px}
.hero .photo{position:absolute;inset:0;background:linear-gradient(120deg,#9fb4c9 0%,#dfe6ee 35%,#7e93ab 60%,#2c3f5c 100%)}
.hero-title{position:absolute;top:300px;left:0;height:64px;padding:0 26px 0 40px;background:var(--blue);color:#fff;font-family:"Oswald",sans-serif;font-weight:500;font-size:42px;line-height:64px;text-transform:uppercase}
.hero-sub{position:absolute;top:364px;left:0;height:46px;padding:0 22px 0 40px;background:rgba(20,30,45,.85);color:#fff;font-family:"Oswald",sans-serif;font-size:28px;line-height:46px}
.hero-arrows{position:absolute;top:432px;left:40px;display:flex;gap:6px}
.arrow-btn{width:34px;height:34px;background:rgba(20,30,45,.85);display:flex;align-items:center;justify-content:center}

/* welcome */
.welcome{top:780px;text-align:center}
.welcome h1{font-size:26px;font-weight:700;text-transform:uppercase;letter-spacing:.5px}
.welcome h1 span{color:var(--blue)}
.welcome p{margin:16px auto 0;width:960px;font-size:13px;line-height:20px;color:var(--muted)}

/* section headings */
.section-head{display:flex;justify-content:space-between;align-items:center;border-bottom:1px solid var(--line);padding-bottom:10px}
.section-head h2{font-size:20px;font-weight:700;text-transform:uppercase}
.section-head h2 span{color:var(--blue)}
.mini-arrows{display:flex;gap:6px}

/* services */
.services{top:915px}
.service-grid{display:grid;grid-template-columns:repeat(4,1fr);gap:24px;margin-top:22px}
.service-card .thumb{height:150px}
.service-card h3{margin-top:14px;font-size:15px;font-weight:700}
.service-card p{margin-top:8px;font-size:12px;line-height:18px;color:var(--muted)}

/* feature */
.feature{top:1280px;height:230px;display:flex;gap:40px}
.feature .visual{width:480px;height:230px;background:radial-gradient(circle at 50% 50%,#cfe1f5,#6f9fd4 70%,#3b6ea9)}
.feature .text{flex:1;padding-top:6px}
.feature h2{font-size:22px;font-weight:700;text-transform:uppercase}
.feature h2 span{color:var(--blue)}
.feature p{margin-top:14px;font-size:13px;line-height:20px;color:var(--muted)}
.btn{display:inline-block;margin-top:18px;background:var(--blue);color:#fff;font-size:13px;font-weight:600;padding:10px 22px}

/* blog */
.blog{top:1560px}
.blog-grid{display:grid;grid-template-columns:1fr 1fr;gap:40px;margin-top:22px}
.post{display:flex;gap:20px}
.post .thumb{width:220px;height:150px;flex:none}
.post h3{font-size:14px;font-weight:700;text-transform:uppercase}
.post .date{font-size:11px;color:var(--blue);margin-top:4px}
.post p{margin-top:8px;font-size:12px;line-height:18px;color:var(--muted)}
.post .more{display:block;margin-top:8px;font-size:12px;font-weight:600;color:var(--blue)}

/* partners */
.partners{top:1850px;height:110px;border-top:1px solid var(--line);border-bottom:1px solid var(--line);display:flex;justify-content:space-around;align-items:center}
.partner{display:flex;align-items:center;gap:10px;font-size:24px;font-weight:600;color:#3a3f46}
.partner i{width:26px;height:26px;border-radius:50%;background:#3a3f46;display:block}

/* footer */
.site-footer{position:absolute;top:1995px;left:0;width:1200px;height:175px;background:var(--blue-dark);color:#c9d4e6}
.footer-cols{position:absolute;left:80px;top:26px;width:1040px;display:grid;grid-template-columns:1fr 1.2fr 1fr 1fr;gap:40px}
.footer-cols h4{color:#fff;font-size:14px;font-weight:700;text-transform:uppercase;margin-bottom:12px}
.footer-cols li{list-style:none;font-size:12px;line-height:20px}
.footer-cols p{font-size:12px;line-height:19px}
.subscribe{display:flex;margin-top:10px}
.subscribe span{flex:1;height:32px;background:#fff}
.subscribe b{background:var(--blue);color:#fff;font-size:12px;padding:0 12px;line-height:32px}
.socials{display:flex;gap:10px;margin-top:12px}
.socials i{width:26px;height:26px;border:1px solid #c9d4e6;border-radius:50%;display:block}
.copyright{position:absolute;top:2170px;left:0;width:1200px;height:50px;background:var(--navy);color:#c9d4e6;font-size:12px;text-align:center;line-height:50px}
</style>
</head>
<body>
<div class="page">

<header class="site-header">
  <svg class="corner" width="110" height="70" viewBox="0 0 110 70"><polygon points="0,0 110,0 110,70" fill="#0d2f66"/></svg>
  <div class="brand"><span class="mark"></span><span class="name">NSG</span></div>
  <nav class="main-nav">
    <span class="active">Home</span><span>About Us</span><span>Services</span><span>Projects</span><span>Blog</span><span>Contacts</span><span class="sep"></span>
    <svg width="18" height="18" viewBox="0 0 18 18"><circle cx="7.5" cy="7.5" r="5.5" fill="none" stroke="#2b2f36" stroke-width="2"/><line x1="11.5" y1="11.5" x2="16" y2="16" stroke="#2b2f36" stroke-width="2"/></svg>
  </nav>
</header>

<section class="hero">
  <div class="photo" role="img" aria-label="Business team reviewing documents at a laptop in a bright office"></div>
  <div class="hero-title">Managed IT Services</div>
  <div class="hero-sub">Group offers technology consultancy</div>
  <div class="hero-arrows">
    <span class="arrow-btn"><svg width="12" height="12" viewBox="0 0 12 12"><polyline points="8,1 3,6 8,11" fill="none" stroke="#fff" stroke-width="2"/></svg></span>
    <span class="arrow-btn"><svg width="12" height="12" viewBox="0 0 12 12"><polyline points="4,1 9,6 4,11" fill="none" stroke="#fff" stroke-width="2"/></svg></span>
  </div>
</section>

<section class="wrap welcome">
  <h1>Welcome to <span>Norvale Solutions Group</span></h1>
  <p>We help growing businesses plan, run and protect their technology. Our team designs networks, manages servers and supports staff every day so your people can focus on their work. From a single office to many sites, we build reliable systems that scale with you, and we explain every step in plain language. Talk to us about consulting, cloud hosting, software and full managed support plans.</p>
</section>

<section class="wrap services">
  <div class="section-head">
    <h2>Our <span>Services</span></h2>
    <div class="mini-arrows">
      <svg width="14" height="14" viewBox="0 0 14 14"><polyline points="9,2 4,7 9,12" fill="none" stroke="#2b2f36" stroke-width="2"/></svg>
      <svg width="14" height="14" viewBox="0 0 14 14"><polyline points="5,2 10,7 5,12" fill="none" stroke="#2b2f36" stroke-width="2"/></svg>
    </div>
  </div>
  <div class="service-grid">
    <article class="service-card"><div class="thumb" role="img" aria-label="Server hardware and network equipment" style="background:linear-gradient(135deg,#4e83c4,#0f3d78)"></div><h3>Technology consulting</h3><p>Clear advice on systems, budgets and plans that fit your business goals.</p></article>
    <article class="service-card"><div class="thumb" role="img" aria-label="Data centre aisle with server racks" style="background:linear-gradient(135deg,#9bb0c6,#3d5470)"></div><h3>Managed IT Services</h3><p>Round the clock monitoring, updates and help desk support for your team.</p></article>
    <article class="service-card"><div class="thumb" role="img" aria-label="Blue lit server room for cloud hosting" style="background:linear-gradient(135deg,#2f6fc0,#0a2a5c)"></div><h3>Cloud Services &amp; Hosting</h3><p>Secure hosting, backups and cloud tools that keep your data within reach.</p></article>
    <article class="service-card"><div class="thumb" role="img" aria-label="Developer working at a desk with a laptop" style="background:linear-gradient(135deg,#c7d2de,#5f7590)"></div><h3>Software Development</h3><p>Custom apps and integrations built around the way your business works.</p></article>
  </div>
</section>

<section class="wrap feature">
  <div class="visual" role="img" aria-label="Globe surrounded by connected devices and service icons"></div>
  <div class="text">
    <h2>Managed <span>IT Services</span></h2>
    <p>Our managed plans cover the full life of your technology. We watch your network, patch your machines and answer calls from your staff, so small problems never turn into long outages. Each plan has a fixed monthly fee, with no surprise bills.</p>
    <p>Every client gets a named engineer, a clear service report each month and a roadmap for future upgrades. We also handle security, licensing and vendor contact on your behalf.</p>
    <span class="btn">Read more</span>
  </div>
</section>

<section class="wrap blog">
  <div class="section-head">
    <h2>Latest <span>Blog</span></h2>
    <div class="mini-arrows">
      <svg width="14" height="14" viewBox="0 0 14 14"><polyline points="9,2 4,7 9,12" fill="none" stroke="#2b2f36" stroke-width="2"/></svg>
      <svg width="14" height="14" viewBox="0 0 14 14"><polyline points="5,2 10,7 5,12" fill="none" stroke="#2b2f36" stroke-width="2"/></svg>
    </div>
  </div>
  <div class="blog-grid">
    <article class="post">
      <div class="thumb" role="img" aria-label="Team meeting around a table with laptops" style="background:linear-gradient(135deg,#a9bccf,#46607e)"></div>
      <div><h3>Simply dummy text</h3><div class="date">24 April 2024</div><p>Five simple steps to keep your office network safe, from strong passwords to regular backups and staff training.</p><span class="more">Read More »</span></div>
    </article>
    <article class="post">
      <div class="thumb" role="img" aria-label="Hands typing on a laptop keyboard" style="background:linear-gradient(135deg,#d3dbe4,#6c819a)"></div>
      <div><h3>Simply dummy text</h3><div class="date">18 April 2024</div><p>Moving to the cloud does not need to be hard. Here is how we plan a calm, step by step migration.</p><span class="more">Read More »</span></div>
    </article>
  </div>
</section>

<section class="wrap partners">
  <span class="partner"><i></i>Pressfield</span>
  <span class="partner"><i></i>Blockwell</span>
  <span class="partner"><i></i>Corvane</span>
  <span class="partner"><i></i>Haldric</span>
  <span class="partner"><i></i>Quarrel</span>
</section>

<footer class="site-footer">
  <div class="footer-cols">
    <div><h4>Links</h4><ul><li>Customer Support</li><li>Documentation</li><li>Resources</li><li>General FAQ</li><li>Partnership</li></ul></div>
    <div><h4>About Us</h4><p>We are a business IT partner helping teams work faster and safer with dependable technology and friendly support.</p></div>
    <div><h4>Get in Touch</h4><p>Address: 214 Harbour Row, Suite 5<br>Norwick NR4 7TQ<br>Phone: 0123 456 7890<br>Email: hello@norvale.example</p></div>
    <div><h4>Newsletter</h4><p>Get our latest tips and news by email.</p><div class="subscribe"><span></span><b>Subscribe</b></div><div class="socials"><i></i><i></i><i></i></div></div>
  </div>
</footer>
<div class="copyright">Copyright © 2024. All Rights Reserved</div>

</div>
</body>
</html>
```